Upgrade website from just a link tree to a full adult content site with payment gateway.

I would like to upgrade my website VelvetQuorra.com and turn it into a pay site with a payment gateway to my content. I would like to use Wordpress. The designer needs to produce a front page with membership sign up link, payment gateway which would then provide access to the content page. We would need to be able to then go in and edit (if necessary) and load all of the content. We would like this to be as easy as possible and already have paid for a Wordpress license. We could simply allow access to our hostmerry/Wordpress account so you can build it once all the details are confirmed. Needs to be simple to upload and have a format all set to go where we would just log in and do it. May need directions or a tutorial to get us started on the path. We are open to suggestions and ideas. We will be providing adult content. Four pages I believe. Front page , gateway video content page and picture content page. The video and picture content goes really just need to be a layout and then we can drop the videos and images in there. You can ask any other relevant questions and we can update the brief. Sorry we are fairly new to this so this is why we are looking to professionals to lead the way. Please look at current webpage for an idea of how we like the current format. It can be replicated or it can be changed. We will market and funnel our online and SoCial accounts to this page on hopes people sign up and pay membership for access to the content past the first page. Check VelvetQuorra.com for an idea of how we want to move forward. Someone goes to page. We would like to see: They can click on member log in if they have already signed up or click join and go to the payment gateway page where they can choose their membership. Once they are paid they produce their log in and lassoed. Sign in and have access to the content pages. One page can be for photos and one page can be for videos. Would consider a live stream if possible but not mandatory. Basically we want to provide content people can view for a fee. A water mark would also be nice to protect our images and video. Also if there is a way to not allow the content to be downloaded. But a water mark would protect that.

Target Market(s)

Adult entertainment

Industry/Entity Type

Adult entertainment

Coding

Coded - Design and coding required

Number of Pages Required

4 page

Font styles to use
Decorative
Script

Colors
E54698
E96AAD
F1A4CE
F9D9EA
FCEFF6
A7469A
B969AE
D3A5CF
EDDBEB
F8F0F9

Requirements
Must have
• Front page. Gateway Payment/membership sign up. Video content page set up and image content page set up. Water mark we can put on content.
Nice to have
• Live video feed capabilities. Watermark.
Should not have
• Free access to the content.

```html
<!DOCTYPE html>
<html lang="en">
<head>
<meta charset="utf-8">
<title>VelvetQuorra – Signup</title>
<link rel="stylesheet" href="https://fonts.googleapis.com/css2?family=Montserrat:wght@300;400;500;600;700&family=Great+Vibes&display=swap">
<style>
  :root {
    --pink: #eea6cf;
    --pink-soft: #f1a4ce;
    --pink-button: #eea6cd;
    --white: #ffffff;
    --bg-dark: #141414;
    --bg-mid: #2b2b2b;
    --footer: #000000;
  }
  * { margin: 0; padding: 0; box-sizing: border-box; }
  html, body { width: 1200px; height: 890px; overflow: hidden; background: var(--footer); }
  body { font-family: "Montserrat", sans-serif; color: var(--white); position: relative; }

  .hero {
    position: absolute; left: 0; top: 0; width: 1200px; height: 798px;
    background:
      radial-gradient(ellipse at 60% 20%, #3d3d3d 0%, transparent 55%),
      radial-gradient(ellipse at 35% 45%, #2a2a2a 0%, transparent 60%),
      linear-gradient(180deg, var(--bg-mid) 0%, var(--bg-dark) 55%, #202020 100%);
  }

  .contact-email {
    position: absolute; left: 912px; top: 24px;
    display: flex; align-items: center; gap: 11px;
    font-size: 13.5px; font-weight: 400;
  }
  .contact-email svg { width: 17px; height: 13px; }

  .brand {
    position: absolute; left: 58px; top: 54px;
    font-size: 30px; font-weight: 400; letter-spacing: 0.5px; color: var(--white);
  }

  .main-nav { position: absolute; top: 58px; left: 0; width: 1200px; height: 26px; }
  .main-nav a {
    position: absolute; top: 0; font-size: 17.5px; font-weight: 400;
    color: var(--white); text-decoration: none;
  }
  .nav-home { left: 590px; }
  .nav-membership { left: 688px; }
  .nav-videos { left: 838px; }
  .nav-gallery { left: 941px; }
  .nav-login {
    left: 1044px !important; top: -0.5px !important;
    width: 57px; height: 25px; line-height: 25px; text-align: center;
    background: var(--pink-button); border-radius: 3px; font-size: 13px !important;
  }

  .page-title {
    position: absolute; left: 0; width: 1200px; top: 148px;
    text-align: center; font-family: "Great Vibes", cursive;
    font-size: 72px; font-weight: 400; color: var(--pink);
  }

  .select-prompt {
    position: absolute; left: 0; width: 1200px; top: 297px;
    text-align: center; font-size: 19px; font-weight: 400;
    letter-spacing: 0.4px; color: var(--pink);
  }

  .plan {
    position: absolute; top: 370px; width: 213px;
    border: 1.5px solid var(--pink);
  }
  .plan-monthly { left: 359px; height: 214px; }
  .plan-yearly { left: 629px; height: 237px; }
  .plan-name {
    position: absolute; top: -11px; padding: 0 5px;
    font-size: 16px; color: var(--pink); line-height: 20px;
    background: transparent;
  }
  .plan-monthly .plan-name { left: 26px; }
  .plan-yearly .plan-name { left: 32px; padding: 0 13px; }
  .plan-name::before {
    content: ""; position: absolute; inset: 0;
    background: #1b1b1b; z-index: -1;
  }
  .plan-name { isolation: isolate; }

  .plan-price {
    position: absolute; top: 30px; left: 32px;
    font-size: 48px; font-weight: 600; color: var(--pink); line-height: 1; letter-spacing: -0.5px;
  }
  .plan-yearly .plan-price { left: 33px; }
  .plan-price sup { font-size: 24px; font-weight: 600; vertical-align: top; position: relative; top: -2px; margin-right: 1px; }
  .plan-term {
    position: absolute; top: 82px; right: 33px;
    font-size: 8px; font-weight: 500; color: var(--pink);
  }
  .plan-yearly .plan-term { right: 34px; }

  .plan-features { position: absolute; left: 29px; top: 101px; list-style: none; color: var(--pink); font-size: 16px; line-height: 18.5px; }
  .plan-monthly .plan-features li { margin-bottom: 6px; }
  .plan-yearly .plan-features li { margin-bottom: 14px; }

  .next-button {
    position: absolute; left: 456px; top: 634px; width: 288px; height: 40px;
    border-radius: 20px; background: var(--pink-button);
    color: var(--white); font-size: 12.5px; font-weight: 400;
    display: flex; align-items: center; justify-content: center; text-decoration: none;
  }

  .site-footer {
    position: absolute; left: 0; top: 798px; width: 1200px; height: 92px;
    background: var(--footer); border-top: 1px solid #e6e6e6;
    display: flex; align-items: center; justify-content: center;
    font-size: 17px; font-weight: 400;
  }
  .site-footer strong { font-weight: 600; }
</style>
</head>
<body>
  <div class="hero" role="img" aria-label="Dark monochrome bedroom photograph filling the background"></div>

  <div class="contact-email">
    <svg viewBox="0 0 17 13" fill="none" stroke="#ffffff" stroke-width="1"><rect x="0.5" y="0.5" width="16" height="12"/><path d="M0.5 0.5 L8.5 7.5 L16.5 0.5 M0.5 12.5 L6.5 6 M16.5 12.5 L10.5 6"/></svg>
    <span>hello@velvetquorra.com</span>
  </div>

  <div class="brand">VelvetQuorra</div>

  <nav class="main-nav">
    <a class="nav-home" href="#">Home</a>
    <a class="nav-membership" href="#">Membership</a>
    <a class="nav-videos" href="#">Videos</a>
    <a class="nav-gallery" href="#">Gallery</a>
    <a class="nav-login" href="#">Login</a>
  </nav>

  <h1 class="page-title">Signup</h1>

  <p class="select-prompt">PLEASE SELECT YOUR MEMBERSHIP:</p>

  <section class="plan plan-monthly">
    <span class="plan-name">Monthly</span>
    <div class="plan-price"><sup>$</sup>24.99</div>
    <div class="plan-term">for one month</div>
    <ul class="plan-features">
      <li>- Unlimited access of<br>Videos and Photos</li>
      <li>- Biweekly online date</li>
      <li>- Sexting</li>
    </ul>
  </section>

  <section class="plan plan-yearly">
    <span class="plan-name">Yearly</span>
    <div class="plan-price"><sup>$</sup>49.99</div>
    <div class="plan-term">for three month recurring</div>
    <ul class="plan-features">
      <li>- All monthly features</li>
      <li>- Daily cam sex</li>
      <li>- Daily sexting</li>
      <li>and much more...</li>
    </ul>
  </section>

  <a class="next-button" href="#">NEXT</a>

  <footer class="site-footer">
    <span>Copyright © 2020-2021 VelvetQuorra | <strong>Privacy</strong> | <strong>Terms</strong></span>
  </footer>
</body>
</html>
```